SkyRavelin Unique Gift Certificate

We need a unique, luxury gift certificate created for our online company (SkyRavelin). We are looking for something out of the ordinary, ie. do not want it to look like a 'normal' gift certificate. Please visit our website to gain a feel for our company (skyravelin.com.au). The dimensions are 148x148mm. We need our logo, website details, to, from, description, code, exp date included. The certificate will be printed on wood veneer so watermarks will not work. We want it to be clean and minimalistic.

Industry/Entity Type

It Company

```html
<!DOCTYPE html>
<html lang="en">
<head>
<meta charset="utf-8">
<title>SkyRavelin Gift Certificate</title>
<link rel="stylesheet" href="https://fonts.googleapis.com/css2?family=Great+Vibes&family=Raleway:wght@300;400&display=swap">
<style>
  :root {
    --page: #efece6;
    --veneer-light: #ecdcab;
    --veneer-mid: #e2cc93;
    --veneer-dark: #d4bb7c;
    --panel: #d9c388;
    --panel-edge: #c9ae6c;
    --ink: #b2935a;
    --ink-soft: #c4a872;
    --line: #a98b55;
    --band: #cfb477;
    --band-text: #ead9a8;
    --badge: #ffffff;
    --badge-edge: #e8892f;
    --logo: #3f8fb5;
  }
  * { box-sizing: border-box; margin: 0; padding: 0; }
  html, body { width: 1200px; height: 927px; overflow: hidden; }
  body { background: var(--page); font-family: "Raleway", sans-serif; position: relative; }

  .certificate {
    position: absolute; left: 190px; top: 53px; width: 820px; height: 820px;
    background: linear-gradient(100deg, var(--veneer-light) 0%, var(--veneer-mid) 45%, var(--veneer-light) 70%, var(--veneer-mid) 100%);
    overflow: hidden;
    box-shadow: 0 6px 18px rgba(0,0,0,.18);
  }
  .title-block { position: absolute; left: 70px; top: 40px; width: 520px; }
  .title {
    font-family: "Great Vibes", cursive; font-size: 92px; color: var(--ink);
    line-height: 1; padding-left: 20px;
  }
  .title-rule { height: 2px; background: var(--ink-soft); margin-top: 8px; }
  .title-rule.thin { height: 1px; margin-top: 6px; width: 90%; }

  .ornament {
    position: absolute; left: 230px; top: 168px; width: 200px; height: 60px;
    background: radial-gradient(ellipse at center, rgba(178,147,90,.45) 0%, rgba(178,147,90,0) 70%);
  }

  .details-panel {
    position: absolute; left: 60px; top: 220px; width: 640px; height: 400px;
    background: var(--panel); border-radius: 26px;
    border: 2px solid var(--panel-edge);
  }
  .details-panel::after {
    content: ""; position: absolute; inset: 10px; border-radius: 18px;
    border: 2px dotted rgba(255,250,230,.55);
  }
  .field-lines { position: absolute; left: 40px; right: 40px; top: 30px; }
  .field {
    display: flex; align-items: flex-end; height: 52px;
    border-bottom: 1px solid var(--line); position: relative;
  }
  .field-label { font-size: 32px; color: var(--ink); letter-spacing: .5px; padding-bottom: 4px; }
  .expiry {
    position: absolute; right: 10px; top: 14px;
    font-size: 22px; color: var(--ink-soft); font-weight: 300;
  }

  .brand-badge {
    position: absolute; right: 0; top: 250px; width: 150px; height: 170px;
    background: var(--badge); border-left: 5px solid var(--badge-edge);
    border-radius: 70px 0 0 70px;
    display: flex; flex-direction: column; align-items: center; justify-content: center; gap: 10px;
  }
  .brand-mark { width: 54px; height: 54px; border-radius: 50%; background: var(--logo); }
  .brand-name { font-size: 20px; color: var(--logo); font-weight: 400; }

  .web-band {
    position: absolute; left: 0; right: 0; bottom: 0; height: 130px;
    background: var(--band); display: flex; align-items: center; padding-left: 60px;
  }
  .web-address { font-size: 66px; font-weight: 300; color: var(--band-text); letter-spacing: 2px; }
</style>
</head>
<body>
  <section class="certificate">
    <div class="title-block">
      <h1 class="title">Gift Certificate</h1>
      <div class="title-rule"></div>
      <div class="title-rule thin"></div>
    </div>
    <div class="ornament" role="img" aria-label="Floral flourish ornament above the details panel"></div>

    <div class="details-panel">
      <div class="field-lines">
        <div class="field"></div>
        <div class="field"></div>
        <div class="field"><span class="field-label">To:</span></div>
        <div class="field"><span class="field-label">From:</span></div>
        <div class="field"><span class="field-label">Description:</span></div>
        <div class="field"><span class="field-label">Code:</span><span class="expiry">Expiration Date</span></div>
      </div>
    </div>

    <div class="brand-badge">
      <span class="brand-mark"></span>
      <span class="brand-name">SkyRavelin</span>
    </div>

    <div class="web-band">
      <p class="web-address">skyravelin.com.au</p>
    </div>
  </section>
</body>
</html>
```